residential/commercial designer. looking to expand customer base.

we need a postcard design for an established residential/commercial interior design firm. TRV Interiors has over 25 yrs experience in creating unique and timeless residential and commercial spaces. offering assistance with cabinet design & furniture, accessories, lighting, plumbing & finish selections in new construction and renovation projects. TRV Interiors has completed projects in New York, California, Florida and Arizona. we will work with clients builder and them to create their personal space. this allows project to progress smoothly and cost effectively.
want postcard simple, straight forward architectural design concept. not whimsical. maybe wanting to incorporate a tag line.
don't expect to include all photos on postcard. looking to your expert opinion on which words and photos should be included on postcard. i know i don't need to say "i want a design that people don't throw away when they receive it"
include: TRV Interiors, Unified Spaces, info@trvinteriorsdemo.com, 555-314-9082 , Maren Dovetti, Principal
please contact me with your questions
Target Market(s)
high end residential, high style commercial
Industry/Entity Type
Residential
Requirements
Must have
- TRV Interior
- Unified Spaces
- info@trvinteriorsdemo.com
- 555-314-9082
- Maren Dovetti, Principal
- best photos with most visual impact.
- use different photos to show design diversity and style
Nice to have
- tag line

```html
<!DOCTYPE html>
<html lang="en">
<head>
<meta charset="utf-8">
<title>TRV Interiors – Postcard</title>
<link href="https://fonts.googleapis.com/css2?family=EB+Garamond:wght@400&family=Open+Sans:wght@400;600;700&display=swap" rel="stylesheet">
<style>
  :root {
    --backdrop: #898989;
    --ink-black: #000000;
    --paper: #ffffff;
    --espresso: #45352b;
    --body-brown: #3b2a20;
    --rule-brown: #6b5545;
    --shadow-grey: #9a9a9a;
    --photo-warm: #8a6f55;
    --photo-dark: #3a2c22;
    --photo-cream: #d9cbb2;
    --photo-cool: #9aa3a8;
  }
  * { margin: 0; padding: 0; box-sizing: border-box; }
  html, body { width: 1200px; height: 900px; overflow: hidden; }
  body { background: var(--backdrop); position: relative; font-family: "Open Sans", Arial, sans-serif; }

  .card { position: absolute; background: var(--paper); overflow: hidden; }
  .card-front { left: 67px; top: 147px; width: 402px; height: 622px; }
  .card-back { left: 517px; top: 248px; width: 622px; height: 404px; }

  .front-gallery { position: absolute; left: 0; top: 0; width: 402px; height: 528px; background: var(--ink-black); }

  .photo-frame { position: absolute; background: var(--paper); padding: 6px; }
  .photo { width: 100%; height: 100%; }
  .photo-kitchen { background: linear-gradient(160deg, #c9b8a0 0%, var(--photo-warm) 45%, var(--photo-dark) 100%); }
  .photo-stair { background: linear-gradient(135deg, #d7d0c4 0%, #8f7a62 50%, #4b3a2c 100%); }
  .photo-range { background: linear-gradient(180deg, #efe6d2 0%, var(--photo-cream) 55%, #8c7a62 100%); }
  .photo-bar { background: linear-gradient(180deg, #cfcac2 0%, #6b5646 45%, #d8c6a0 75%, #e4e1dc 100%); }
  .photo-library { background: linear-gradient(135deg, #d8cfbd 0%, #a99a80 50%, #4a3b30 100%); }
  .photo-bath { background: radial-gradient(ellipse at 50% 55%, #8aa6c8 0%, #3a2c24 45%, #d9d4cc 100%); }
  .photo-vaulted { background: linear-gradient(180deg, #3b2b20 0%, #8b7257 55%, #cfc3b0 100%); }
  .photo-white-kitchen { background: linear-gradient(180deg, #f1ede6 0%, #d6cfc4 60%, #3d342e 100%); }
  .photo-wine { background: linear-gradient(90deg, #6d4a31 0%, #a98a6a 50%, var(--photo-cool) 100%); }

  .front-footer { position: absolute; left: 0; top: 528px; width: 402px; height: 94px; background: var(--paper); }
  .tagline { position: absolute; left: 16px; top: 26px; color: var(--ink-black); line-height: 1.05; }
  .tagline-line1 { font-size: 20px; }
  .tagline-line2 { font-size: 16px; padding-left: 2px; }

  .brand-shadow { position: absolute; left: 228px; top: 508px; width: 150px; height: 112px; background: var(--shadow-grey); transform: rotate(-2deg); }
  .brand-block { position: absolute; left: 234px; top: 508px; width: 149px; height: 114px; background: var(--espresso); color: var(--paper); font-family: "EB Garamond", Georgia, serif; font-weight: 400; text-align: center; }
  .brand-name { position: absolute; left: 0; top: 12px; width: 149px; font-size: 30px; line-height: 32px; }
  .brand-sub { position: absolute; left: 0; top: 80px; width: 149px; font-size: 13px; }

  .back-band { position: absolute; left: 0; top: 0; width: 522px; height: 81px; background: var(--ink-black); }
  .stamp-box { position: absolute; left: 543px; top: 26px; width: 57px; height: 75px; border: 1px solid var(--rule-brown); }
  .address-line { position: absolute; left: 439px; width: 161px; height: 1px; background: var(--rule-brown); }

  .back-copy { position: absolute; left: 27px; top: 117px; width: 377px; font-size: 12.3px; line-height: 16.5px; color: var(--body-brown); text-align: justify; }
  .back-copy p { margin-bottom: 5px; }
  .back-copy strong { font-weight: 700; }
  .back-copy .cta-head { font-weight: 700; margin-bottom: 0; }

  .contact-box { position: absolute; left: 29px; top: 330px; width: 240px; height: 63px; background: var(--espresso); color: var(--paper); font-weight: 700; padding: 4px 0 0 48px; }
  .contact-row { display: flex; align-items: center; gap: 5px; font-size: 12px; line-height: 17px; }
  .contact-email { text-decoration: underline; }
  .contact-row svg { width: 13px; height: 11px; flex: none; }
  .contact-name { font-size: 13.5px; line-height: 20px; }
</style>
</head>
<body>

<section class="card card-front" aria-label="Postcard front">
  <div class="front-gallery">
    <div class="photo-frame" style="left:16px;top:35px;width:180px;height:124px;"><div class="photo photo-kitchen" role="img" aria-label="Modern kitchen with stone wall, island and bar stools"></div></div>
    <div class="photo-frame" style="left:204px;top:35px;width:180px;height:124px;"><div class="photo photo-stair" role="img" aria-label="Open staircase with glass railing and stone wall"></div></div>
    <div class="photo-frame" style="left:16px;top:180px;width:132px;height:154px;"><div class="photo photo-range" role="img" aria-label="Cream cabinetry around a range hood and cooktop"></div></div>
    <div class="photo-frame" style="left:160px;top:180px;width:226px;height:156px;"><div class="photo photo-bar" role="img" aria-label="Lounge with illuminated bar and high stools"></div></div>
    <div class="photo-frame" style="left:16px;top:356px;width:180px;height:125px;"><div class="photo photo-library" role="img" aria-label="Home library with built-in bookshelves"></div></div>
    <div class="photo-frame" style="left:204px;top:356px;width:180px;height:125px;"><div class="photo photo-bath" role="img" aria-label="Marble bathroom with freestanding tub"></div></div>
  </div>
  <div class="front-footer">
    <div class="tagline">
      <div class="tagline-line1">Transforming spaces</div>
      <div class="tagline-line2">into a lifestyle statement.</div>
    </div>
  </div>
  <div class="brand-shadow"></div>
  <div class="brand-block">
    <div class="brand-name">TRV<br>Interiors</div>
    <div class="brand-sub">Unified Spaces</div>
  </div>
</section>

<section class="card card-back" aria-label="Postcard back">
  <div class="back-band"></div>
  <div class="photo-frame" style="left:27px;top:21px;width:139px;height:88px;"><div class="photo photo-vaulted" role="img" aria-label="Great room with vaulted timber ceiling and kitchen"></div></div>
  <div class="photo-frame" style="left:203px;top:21px;width:125px;height:88px;"><div class="photo photo-white-kitchen" role="img" aria-label="White kitchen with pendant lights"></div></div>
  <div class="photo-frame" style="left:363px;top:21px;width:133px;height:88px;"><div class="photo photo-wine" role="img" aria-label="Arched wine cellar door and stone wall with shelves"></div></div>

  <div class="stamp-box"></div>
  <div class="address-line" style="top:196px;"></div>
  <div class="address-line" style="top:221px;"></div>
  <div class="address-line" style="top:246px;"></div>
  <div class="address-line" style="top:271px;"></div>

  <div class="back-copy">
    <p><strong>TRV Interiors</strong> has over 25 years experience in creating unique and timeless <strong>residential</strong> and <strong>commercial</strong> spaces.</p>
    <p>Offering assistance with cabinet design &amp; furniture, accessories, lighting, plumbing &amp; finish selections in <strong>new construction</strong> and <strong>renovation</strong> projects, <strong>TRV Interiors</strong> has completed projects in New York, California, Florida and Arizona.</p>
    <p>We will work with your builder and yourself to create your personal space. This will allow your project to progress <strong>smoothly</strong> and <strong>cost effectively</strong>.</p>
    <p class="cta-head">Ready to make a statement in style?</p>
    <p><strong>Contact us</strong> to discuss your needs and let our vision bring your everyday space to the style you deserve to live in.</p>
  </div>

  <div class="contact-box">
    <div class="contact-row">
      <svg viewBox="0 0 13 11" aria-hidden="true"><rect x="0.5" y="1.5" width="12" height="8" fill="none" stroke="#fff" stroke-width="1.2"/><path d="M0.5 1.5 L6.5 6 L12.5 1.5" fill="none" stroke="#fff" stroke-width="1.2"/></svg>
      <span class="contact-email">info@trvinteriorsdemo.com</span>
    </div>
    <div class="contact-row">
      <svg viewBox="0 0 13 11" aria-hidden="true"><path d="M1 4 Q6.5 -1 12 4 L10 5 L9 3.5 Q6.5 2.5 4 3.5 L3 5 Z" fill="#fff"/><rect x="2.5" y="5.5" width="8" height="5" fill="#fff"/></svg>
      <span>555-314-9082</span>
    </div>
    <div class="contact-name">Maren Dovetti, Principal</div>
  </div>
</section>

</body>
</html>
```